Reboot of current Powerpoint Design

We would like to modernise our current powerpoint design which we use for the delivery of class room based training to 5-10 trainees at a time. We have attached our current design but would like a more updated (yet still practical for in-house edits and development).
We would like to be left with a collection of no more than 10-20 master slides for ongoing use in the business. Critically the slides should be focussed on being able to be easily read in a classroom environment, have minimal or no animation (easy to operate by a trainer) and should recognise our customer base which is largely fairly conservative (heavy industry).
In short we are seeking a professional and engaging end result which mirrors our current branding.
Across our entire range of courses we will use the following key structure:
- Title
- Introductory slides
- Overviews
- Modules
- Content
- Discussion
- Conclusion
As part of this update we would like to increase our use of photos (noting that we are not limited to the photos in the current powerpoint so any design should simply use placeholders).
The updated version should incorporate our current branding which is represented in the attached example powerpoint as well as our website (www.brightlaneskills.com).
Thanks
Glen
Updates
Target Market(s)
Safety and compliance in heavy industries (eg. mining, manufacturing, construction, etc.)
Industry/Entity Type
Training
Font styles to use
Other font styles liked:
- Helvetica (or similar to be used on windows machines)
Colors
Designer to choose colors to be used in the design.
Requirements
Must have
- Approximately 20 master slides that can be easily applied across a large number of current power point presentations.
- Strong visual focus with main use in classroom environment (so note that these are used on a projector screen - please take into account (eg. no small fonts).
- We generally use the notes section for any detailed information (trainer benefit) so our focus is on using the slides as triggers for conversations, training structure and headline topics.
- If anything we are focussed on a less is more mentality and are looking for a clean, simple and professional appeal. Note we have no issue in some of the content of the example slides (CPR) moving to the notes section.
- We have also just begun implementing a new brand bi-line which is:
- PlanWell. MoveWell. BuildWell. (Note the Safe. in each word is in BOLD).
- This bi-line needs to be incorporated along with the Brightlane Skills logo in each slide. Please note that we also use the unique A design in the Brightlane Skills logo as a further design feature in our branding documents. As per current powerpoint, we would prefer this to be incorporated as well.
Nice to have
- Functional graphics (easy to edit) and branded icons to ensure we continue to push the Brightlane Skills brand throughout the presentations.
Should not have
- Animation and difficult to edit slides.

```html
<!DOCTYPE html>
<html lang="en">
<head>
<meta charset="utf-8">
<title>Brightlane Skills – Training Slide Masters</title>
<link href="https://fonts.googleapis.com/css2?family=Roboto+Slab:wght@300;400;700&family=Open+Sans:wght@300;400;600;700&family=Montserrat:wght@700;800&display=swap" rel="stylesheet">
<style>
:root{
  --red:#e5232b;--red-dark:#b8141c;--navy:#262a35;--grey:#9a9ca3;--line:#d9dadd;
  --text:#3a3d45;--muted:#8b8e95;--canvas:#dcdcde;--white:#fff;
}
*{box-sizing:border-box}
html,body{margin:0;padding:0}
body{width:1200px;height:858px;overflow:hidden;background:var(--canvas);position:relative;font-family:'Open Sans',sans-serif;color:var(--text)}
.slide{position:absolute;width:294px;height:166px;background:var(--white);overflow:hidden}
.slide>*{position:absolute;margin:0}
.c1{left:5px}.c2{left:303px}.c3{left:602px}.c4{left:900px}
.r1{top:5px}.r2{top:175px}.r3{top:346px}.r4{top:516px}.r5{top:686px}
.mark{left:20px;top:0;display:flex;gap:1px}
.mark i{display:block;width:5px;height:6px;background:var(--red)}
.mark i:nth-child(2){background:var(--grey)}
.mark i:nth-child(3){background:var(--navy);width:3px}
.title{left:20px;top:9px;font:300 10px/1.2 'Roboto Slab',serif;color:var(--navy)}
.title b{font-weight:700}
.tag{right:14px;top:8px;font:700 4px/1.1 'Open Sans',sans-serif;color:#d6d7da;text-align:right;letter-spacing:.2px}
.foot{left:0;right:0;bottom:0;height:7px;background:var(--navy);font-size:2.6px;color:#7b7f88;text-align:center;line-height:7px}
.foot .page{position:absolute;right:18px;top:0;width:12px;height:7px;background:var(--red);color:#fff;font-size:3px}
.tiny{font-size:3px;line-height:1.45;color:var(--muted)}
.red{color:var(--red)}
.num{font:400 8px/1 'Roboto Slab',serif;color:var(--grey)}
.item .num{display:block}
.item .lbl{display:block;font-size:4.2px;color:var(--red);border-bottom:.4px solid var(--line);padding-bottom:1px;margin:1px 0}
.item .cap{display:block;font-size:2.6px;font-weight:700;color:var(--navy)}
.item .tiny{display:block;width:70px}
.pack{font:700 3.4px/1.2 'Open Sans',sans-serif;color:var(--navy);text-align:center}
.pack .tiny{font-weight:400;display:block;margin-top:2px}
.photo{background:linear-gradient(135deg,#8d8672,#5d5a4f 55%,#b9a88a)}
.brand{display:flex;align-items:center;gap:2px;font:800 8.5px/1 'Montserrat',sans-serif;color:var(--navy);letter-spacing:.2px}
.brand i{display:block;width:5px;height:5px;background:var(--red);flex:none}
.brand-stack{align-items:flex-start;font-size:7.5px;line-height:1.05}
.brand-stack i{margin-top:1px}
.byline{font-size:2.8px;color:var(--muted)}
.bars{display:flex;gap:2px}
.bars i{display:block;width:5px;background:var(--navy);height:100%}
.bars i+i{background:var(--red);width:4px}
.agenda{border-collapse:collapse;font-size:3.2px;color:var(--muted)}
.agenda td{padding:1.6px 4px;border-bottom:.4px solid var(--line)}
.agenda .head td{color:var(--red);font:400 5px 'Roboto Slab',serif;border-bottom:.5px dashed var(--grey)}
.agenda .n{text-align:center;width:14px}
.agenda .v{text-align:right}
ul.bul{list-style:none;padding:0}
ul.bul li{font-size:2.9px;color:var(--muted);margin-bottom:2.6px;padding-left:5px;position:relative}
ul.bul li::before{content:"";position:absolute;left:0;top:.8px;width:1.5px;height:1.5px;border-radius:50%;background:var(--red)}
.grid-table{border-collapse:collapse;font-size:2.6px;width:254px}
.grid-table td,.grid-table th{height:9.5px;border-bottom:.4px solid #fff;padding:0 3px;color:var(--muted);text-align:left}
.grid-table th{background:#9fa1a6;color:#e9e9ea;font-weight:600}
.grid-table tr:nth-child(even) td{background:#f2f2f3}
.grid-table tr td.feat{background:var(--red);color:#fff;text-align:center;width:75px}
.grid-table .ok{color:#7bb543}.grid-table .no{color:var(--red)}
</style>
</head>
<body>

<!-- 1 cover -->
<section class="slide c1 r1">
  <div class="bars" style="left:24px;top:0;height:66px"><i></i><i></i></div>
  <div class="bars" style="left:24px;top:133px;height:33px"><i></i><i></i></div>
  <div class="photo" role="img" aria-label="Faint line drawing of a construction crane and building frame" style="left:150px;top:0;width:144px;height:159px;background:linear-gradient(160deg,#fff 10%,#eeeff1 70%,#e4e5e8)"></div>
  <div class="brand" style="left:20px;top:74px"><i></i>BRIGHTLANE SKILLS</div>
  <h1 style="left:20px;top:97px;font:700 7.6px 'Roboto Slab',serif;color:var(--navy)">Cardiopulmonary Resuscitation</h1>
  <p style="left:20px;top:107px;font-size:4px;color:var(--muted)">Place the lorem ipsum subtitle here</p>
  <p class="tiny" style="left:20px;top:117px">Presented by: Mara Quinn<br>mara.quinn@mail.com</p>
</section>

<!-- 2 agenda -->
<section class="slide c2 r1">
  <div class="mark"><i></i><i></i><i></i></div>
  <h2 class="title"><b>Course</b> Agenda</h2>
  <div style="left:20px;top:22px;width:18px;height:1px;background:var(--red)"></div>
  <div class="tag">BRIGHTLANE<br>SKILLS</div>
  <table class="agenda" style="left:48px;top:44px;width:226px">
    <tr class="head"><td class="n">I</td><td colspan="2">Introduction Housekeeping</td></tr>
    <tr><td class="n">1</td><td>Plan each task before you start the day</td><td class="v">5</td></tr>
    <tr><td class="n">2</td><td>Check the area and the tools you need</td><td class="v">10</td></tr>
    <tr><td class="n">3</td><td>Talk through risks with your team</td><td class="v">15</td></tr>
    <tr class="head"><td class="n">II</td><td colspan="2">Section Dolor Sit Amet</td></tr>
    <tr><td class="n">1</td><td>Talk through risks with your team</td><td class="v">5</td></tr>
    <tr><td class="n">2</td><td>Check the area and the tools you need</td><td class="v">10</td></tr>
    <tr><td class="n">3</td><td>Plan each task before you start the day</td><td class="v">15</td></tr>
  </table>
  <footer class="foot">www.brightlaneskills.com<span class="page">2</span></footer>
</section>

<!-- 3 section -->
<section class="slide c3 r1">
  <div class="bars" style="left:20px;top:0;height:110px"><i></i><i></i></div>
  <table class="agenda" style="left:65px;top:30px;width:206px">
    <tr class="head"><td class="n">I</td><td colspan="2">Introduction Housekeeping</td></tr>
    <tr><td class="n">1</td><td>Plan each task before you start the day</td><td class="v">5</td></tr>
    <tr><td class="n">2</td><td>Check the area and the tools you need</td><td class="v">10</td></tr>
    <tr><td class="n">3</td><td>Talk through risks with your team</td><td class="v">15</td></tr>
    <tr><td class="n">4</td><td>Review the job when work is done</td><td class="v">20</td></tr>
  </table>
  <div class="brand brand-stack" style="left:20px;top:119px"><i></i><span>BRIGHTLANE<br>SKILLS</span></div>
  <p class="byline" style="left:20px;top:138px">PlanWell. MoveWell. BuildWell.</p>
  <div style="left:90px;top:118px;width:.5px;height:24px;background:var(--line)"></div>
  <h2 style="left:95px;top:121px;font:700 7.5px 'Roboto Slab',serif;color:var(--navy)">Perform CPR procedures</h2>
  <p style="left:95px;top:132px;font-size:4px;color:var(--grey)">Lorem ipsum subtitle goes here</p>
  <footer class="foot">www.brightlaneskills.com<span class="page">3</span></footer>
</section>

<!-- 4 quote -->
<section class="slide c4 r1">
  <div class="mark"><i></i><i></i><i></i></div>
  <h2 class="title"><b>Quote</b> Slides</h2>
  <div class="tag">BRIGHTLANE<br>SKILLS</div>
  <div style="left:0;right:0;top:30px;text-align:center;font:700 16px 'Roboto Slab',serif;color:var(--red)">“</div>
  <blockquote style="left:0;right:0;top:60px;text-align:center;font:300 12.5px/1.4 'Open Sans',sans-serif;color:#4a4d55">Any attempt at<br>resuscitation is better<br>than no attempt</blockquote>
  <div style="left:0;right:0;top:114px;text-align:center;font:700 16px 'Roboto Slab',serif;color:var(--red)">”</div>
  <footer class="foot">www.brightlaneskills.com<span class="page">4</span></footer>
</section>

<!-- 5 respond photo -->
<section class="slide c1 r2">
  <div class="mark"><i></i><i></i><i></i></div>
  <h2 class="title"><b>Emergency</b> Respond</h2>
  <div class="tag">BRIGHTLANE<br>SKILLS</div>
  <div class="photo" role="img" aria-label="Photo placeholder: worker giving chest compressions on a site" style="left:20px;top:29px;width:97px;height:117px"></div>
  <div style="left:20px;top:135px;width:97px;height:11px;background:var(--red);color:#fff;font-size:4.5px;text-align:center;line-height:11px">Some title goes here</div>
  <div style="left:148px;top:37px;width:2px;height:3px;background:var(--red)"></div>
  <h3 style="left:148px;top:41px;font:700 7.5px/1.2 'Roboto Slab',serif;color:var(--navy)">Respond to an<br>emergency<br>situation</h3>
  <p class="tiny" style="left:148px;top:80px;width:122px">Call for help, check the scene is safe and start care quickly. Keep calm and follow each step you have been trained to use on site.</p>
  <ul class="bul" style="left:150px;top:111px;width:120px">
    <li>This is a sample text here. Insert your text here.</li>
    <li>Insert your desired text here. Insert your text here.</li>
    <li>This is a sample text here. Insert your text here.</li>
  </ul>
  <footer class="foot">www.brightlaneskills.com<span class="page">5</span></footer>
</section>

<!-- 6 respond red photo -->
<section class="slide c2 r2">
  <div class="mark"><i></i><i></i><i></i></div>
  <h2 class="title"><b>Emergency</b> Respond</h2>
  <div class="tag">BRIGHTLANE<br>SKILLS</div>
  <div role="img" aria-label="Photo placeholder with red overlay: hands performing CPR" style="left:20px;top:35px;width:190px;height:107px;background:linear-gradient(120deg,#c81821,#e5403f 50%,#f0706a)"></div>
  <h3 style="left:34px;top:65px;font:700 5.5px/1.3 'Roboto Slab',serif;color:#fff">Respond to an<br>emergency situation</h3>
  <p style="left:34px;top:82px;width:150px;font-size:3px;line-height:1.5;color:#fde0df">Check the scene, call for help and begin chest compressions at a steady pace. Keep going until trained help arrives and takes over the care.</p>
  <div class="item" style="left:222px;top:35px"><span class="num" style="color:var(--navy)">01</span><span class="lbl">Análisis Interno</span><span class="cap">INFOGRAPHIC YOUR TEXT</span><span class="tiny">Short note for this step here</span></div>
  <div class="item" style="left:222px;top:70px"><span class="num" style="color:var(--navy)">02</span><span class="lbl">Análisis Interno</span><span class="cap">INFOGRAPHIC YOUR TEXT</span><span class="tiny">Short note for this step here</span></div>
  <div class="item" style="left:222px;top:105px"><span class="num" style="color:var(--navy)">03</span><span class="lbl">Análisis Interno</span><span class="cap">INFOGRAPHIC YOUR TEXT</span><span class="tiny">Short note for this step here</span></div>
  <footer class="foot">www.brightlaneskills.com<span class="page">6</span></footer>
</section>

<!-- 7 respond grid + photo -->
<section class="slide c3 r2">
  <div class="mark"><i></i><i></i><i></i></div>
  <h2 class="title"><b>Emergency</b> Respond</h2>
  <p class="tiny" style="left:20px;top:33px;width:150px">Keep the casualty still, check breathing and start care quickly. Send a second person to bring the first aid kit and the defibrillator to the scene.</p>
  <div class="item" style="left:20px;top:61px"><span class="num">01</span><span class="lbl">Análisis Interno</span><span class="cap">INFOGRAPHIC YOUR TEXT</span><span class="tiny">Short note for this step here</span></div>
  <div class="item" style="left:106px;top:61px"><span class="num">03</span><span class="lbl">Análisis Interno</span><span class="cap">INFOGRAPHIC YOUR TEXT</span><span class="tiny">Short note for this step here</span></div>
  <div class="item" style="left:20px;top:106px"><span class="num">02</span><span class="lbl">Análisis Interno</span><span class="cap">INFOGRAPHIC YOUR TEXT</span><span class="tiny">Short note for this step here</span></div>
  <div class="item" style="left:106px;top:106px"><span class="num">04</span><span class="lbl">Análisis Interno</span><span class="cap">INFOGRAPHIC YOUR TEXT</span><span class="tiny">Short note for this step here</span></div>
  <div class="photo" role="img" aria-label="Photo placeholder: workers in hard hats using a defibrillator" style="left:176px;top:0;width:118px;height:159px"></div>
  <footer class="foot">www.brightlaneskills.com<span class="page">7</span></footer>
</section>

<!-- 8 respond illustration -->
<section class="slide c4 r2">
  <div class="mark"><i></i><i></i><i></i></div>
  <h2 class="title"><b>Emergency</b> Respond</h2>
  <div class="tag">BRIGHTLANE<br>SKILLS</div>
  <div class="item" style="left:20px;top:38px"><span class="num">01</span><span class="lbl">Análisis Interno</span><span class="cap">INFOGRAPHIC YOUR TEXT</span><span class="tiny">Short note for this step here</span></div>
  <div class="item" style="left:20px;top:119px"><span class="num">02</span><span class="lbl">Análisis Interno</span><span class="cap">INFOGRAPHIC YOUR TEXT</span><span class="tiny">Short note for this step here</span></div>
  <div class="item" style="left:214px;top:38px"><span class="num">03</span><span class="lbl">Análisis Interno</span><span class="cap">INFOGRAPHIC YOUR TEXT</span><span class="tiny">Short note for this step here</span></div>
  <div class="item" style="left:214px;top:119px"><span class="num">04</span><span class="lbl">Análisis Interno</span><span class="cap">INFOGRAPHIC YOUR TEXT</span><span class="tiny">Short note for this step here</span></div>
  <div role="img" aria-label="Illustration placeholder: rescuer kneeling beside a casualty giving CPR" style="left:95px;top:55px;width:110px;height:72px;border-radius:40%;background:radial-gradient(ellipse at center,#c9ccd3,#eef0f3 70%,#fff)"></div>
  <footer class="foot">www.brightlaneskills.com<span class="page">8</span></footer>
</section>

<!-- 9 process -->
<section class="slide c1 r3">
  <div class="mark"><i></i><i></i><i></i></div>
  <h2 class="title"><b>Perform</b> Procedure</h2>
  <div class="tag">BRIGHTLANE<br>SKILLS</div>
  <svg style="left:0;top:0" width="294" height="166" viewBox="0 0 294 166" aria-hidden="true">
    <g fill="none" stroke="#e5232b" stroke-width="1.6">
      <path d="M40 64 C45 40 102 40 107 64"/>
      <path d="M107 90 C112 115 165 115 170 90"/>
      <path d="M170 64 C175 40 227 40 232 64"/>
    </g>
    <g fill="#e5232b"><polygon points="104,61 110,61 107,66"/><polygon points="167,93 173,93 170,88"/><polygon points="229,61 235,61 232,66"/></g>
    <g fill="#262a35"><circle cx="40" cy="77" r="13"/><circle cx="107" cy="77" r="13"/><circle cx="170" cy="77" r="13"/><circle cx="232" cy="77" r="13"/></g>
    <g fill="#fff"><circle cx="38" cy="71" r="2.5"/><path d="M33 78 q5 -5 10 0z"/><path d="M107 67 l-3.5 5 a3.6 3.6 0 1 0 7 0z"/><path d="M166 75 q4 -8 8 -6 q-2 5 -8 6z"/><path d="M228 75 q4 -7 9 -6 q-3 6 -9 6z"/></g>
    <g font-size="2.3" fill="#c9ccd3" text-anchor="middle" font-family="Open Sans"><text x="40" y="84">Lorem of</text><text x="107" y="84">Lorem of</text><text x="170" y="84">Lorem of</text><text x="232" y="84">Lorem of</text></g>
  </svg>
  <div class="item" style="left:99px;top:30px"><span class="num">02</span><span class="lbl">Análisis Interno</span><span class="cap">INFOGRAPHIC YOUR TEXT</span><span class="tiny">Short note for this step</span></div>
  <div class="item" style="left:230px;top:30px"><span class="num">04</span><span class="lbl">Análisis Interno</span><span class="cap">INFOGRAPHIC YOUR TEXT</span><span class="tiny" style="width:50px">Short note for this step</span></div>
  <div class="item" style="left:56px;top:84px"><span class="num">01</span><span class="lbl">Análisis Interno</span><span class="cap">INFOGRAPHIC YOUR TEXT</span><span class="tiny">Short note for this step</span></div>
  <div class="item" style="left:188px;top:84px"><span class="num">03</span><span class="lbl">Análisis Interno</span><span class="cap">INFOGRAPHIC YOUR TEXT</span><span class="tiny">Short note for this step</span></div>
  <p class="tiny" style="left:30px;right:30px;top:134px;text-align:center;color:#555">Each step builds on the last. Work through the procedure in order, check in with your partner and swap roles when you tire so care stays strong until help arrives.</p>
  <footer class="foot">www.brightlaneskills.com<span class="page">9</span></footer>
</section>

<!-- 10 iconic outline -->
<section class="slide c2 r3">
  <div class="mark"><i></i><i></i><i></i></div>
  <h2 class="title"><b>Iconic</b> Point</h2>
  <div class="tag">BRIGHTLANE<br>SKILLS</div>
  <svg style="left:0;top:0" width="294" height="166" viewBox="0 0 294 166" aria-hidden="true">
    <g fill="none" stroke="#e5232b" stroke-width=".8">
      <circle cx="50" cy="50" r="10"/><circle cx="144" cy="50" r="10"/><circle cx="238" cy="50" r="10"/>
      <circle cx="50" cy="104" r="10"/><circle cx="144" cy="104" r="10"/><circle cx="238" cy="104" r="10"/>
      <path d="M50 55 c-4 -5 -4 -9 0 -9 c4 0 4 4 0 9z"/><circle cx="50" cy="49" r="1.2"/>
      <rect x="139" y="47" width="10" height="7" rx="1"/><circle cx="144" cy="50.5" r="2"/>
      <path d="M238 55 l-4 -4 a2.4 2.4 0 0 1 4 -3 a2.4 2.4 0 0 1 4 3z"/>
      <path d="M46 102 h2 l4 -3 v10 l-4 -3 h-2z"/><path d="M54 101 q2 3 0 6"/>
      <path d="M140 107 h8 l-1 -2 v-3 a3 3 0 0 0 -6 0 v3z"/>
      <path d="M234 106 l4 -6 h4 v4 l-6 4z"/>
    </g>
  </svg>
  <div class="pack" style="left:20px;top:63px;width:60px">ORGANIZE PACK<span class="tiny">Short note to sum up this idea</span></div>
  <div class="pack" style="left:114px;top:63px;width:60px">ORGANIZE PACK<span class="tiny">Short note to sum up this idea</span></div>
  <div class="pack" style="left:208px;top:63px;width:60px">ORGANIZE PACK<span class="tiny">Short note to sum up this idea</span></div>
  <div class="pack" style="left:20px;top:117px;width:60px">ORGANIZE PACK<span class="tiny">Short note to sum up this idea</span></div>
  <div class="pack" style="left:114px;top:117px;width:60px">ORGANIZE PACK<span class="tiny">Short note to sum up this idea</span></div>
  <div class="pack" style="left:208px;top:117px;width:60px">ORGANIZE PACK<span class="tiny">Short note to sum up this idea</span></div>
  <footer class="foot">www.brightlaneskills.com<span class="page">10</span></footer>
</section>

<!-- 11 iconic line -->
<section class="slide c3 r3">
  <div class="mark"><i></i><i></i><i></i></div>
  <h2 class="title"><b>Iconic</b> Point</h2>
  <div class="tag">BRIGHTLANE<br>SKILLS</div>
  <div style="left:0;right:0;top:94px;height:1.5px;background:var(--red)"></div>
  <svg style="left:0;top:0" width="294" height="166" viewBox="0 0 294 166" aria-hidden="true">
    <g fill="#fff" stroke="#e5232b" stroke-width=".8">
      <circle cx="37" cy="70" r="17"/><circle cx="110" cy="70" r="17"/><circle cx="183" cy="70" r="17"/><circle cx="256" cy="70" r="17"/>
    </g>
    <g fill="none" stroke="#262a35" stroke-width=".7">
      <ellipse cx="37" cy="69" rx="5" ry="3.5"/><path d="M34 72 l-1 3 3 -2"/>
      <path d="M110 74 v-2 a4 4 0 1 1 0.1 0"/><path d="M108.5 76 h3"/>
      <rect x="178" y="65" width="10" height="10" transform="rotate(45 183 70)"/>
      <path d="M251 68 h3 l5 -3 v10 l-5 -3 h-3z"/>
    </g>
  </svg>
  <div class="pack" style="left:7px;top:106px;width:60px">ORGANIZE PACK<span class="tiny">Short note to sum up this idea</span></div>
  <div class="pack" style="left:80px;top:106px;width:60px">ORGANIZE PACK<span class="tiny">Short note to sum up this idea</span></div>
  <div class="pack" style="left:153px;top:106px;width:60px">ORGANIZE PACK<span class="tiny">Short note to sum up this idea</span></div>
  <div class="pack" style="left:226px;top:106px;width:60px">ORGANIZE PACK<span class="tiny">Short note to sum up this idea</span></div>
  <footer class="foot">www.brightlaneskills.com<span class="page">11</span></footer>
</section>

<!-- 12 iconic filled -->
<section class="slide c4 r3">
  <div class="mark"><i></i><i></i><i></i></div>
  <h2 class="title"><b>Iconic</b> Point</h2>
  <div class="tag">BRIGHTLANE<br>SKILLS</div>
  <svg style="left:0;top:0" width="294" height="166" viewBox="0 0 294 166" aria-hidden="true">
    <g fill="#e5232b" stroke="#f3c9cb" stroke-width="1.5">
      <circle cx="58" cy="50" r="16"/><circle cx="147" cy="50" r="16"/><circle cx="235" cy="50" r="16"/>
    </g>
    <g fill="none" stroke="#fff" stroke-width=".8">
      <circle cx="58" cy="50" r="3"/><circle cx="58" cy="50" r="5.5" stroke-dasharray="2 1.5"/>
      <path d="M147 56 a4 4 0 0 1 -4 -4 c0 -3 3 -4 3 -8 c3 2 5 5 5 8 a4 4 0 0 1 -4 4z"/>
      <path d="M229 52 l12 -7 -4 12 -3 -4z"/>
    </g>
  </svg>
  <div class="pack" style="left:28px;top:75px;width:60px;border-bottom:.4px solid var(--line);padding-bottom:2px">ORGANIZE PACK</div>
  <div class="pack" style="left:117px;top:75px;width:60px;border-bottom:.4px solid var(--line);padding-bottom:2px">ORGANIZE PACK</div>
  <div class="pack" style="left:205px;top:75px;width:60px;border-bottom:.4px solid var(--line);padding-bottom:2px">ORGANIZE PACK</div>
  <ul class="bul" style="left:26px;top:84px;width:64px"><li>Keep the work area clear of trip risks</li><li>Wear the right gear for each task</li><li>Report any near miss to your lead</li></ul>
  <ul class="bul" style="left:115px;top:84px;width:64px"><li>Keep the work area clear of trip risks</li><li>Wear the right gear for each task</li><li>Report any near miss to your lead</li></ul>
  <ul class="bul" style="left:203px;top:84px;width:64px"><li>Keep the work area clear of trip risks</li><li>Wear the right gear for each task</li><li>Report any near miss to your lead</li></ul>
  <footer class="foot">www.brightlaneskills.com<span class="page">12</span></footer>
</section>

<!-- 13 line chart -->
<section class="slide c1 r4">
  <div class="mark"><i></i><i></i><i></i></div>
  <h2 class="title"><b>Data</b> Driven</h2>
  <div class="tag">BRIGHTLANE<br>SKILLS</div>
  <svg style="left:18px;top:44px" width="168" height="104" viewBox="0 0 168 104" aria-label="Line chart of two series from January to August">
    <g font-size="3" fill="#8b8e95" font-family="Open Sans"><text x="70" y="5">○ Series 1  ○ Series 2</text>
      <text x="0" y="23">7</text><text x="0" y="34">6</text><text x="0" y="45">5</text><text x="0" y="56">4</text><text x="0" y="67">3</text><text x="0" y="78">2</text><text x="0" y="89">1</text><text x="0" y="100">0</text>
      <text x="10" y="104">JAN</text><text x="30" y="104">FEB</text><text x="50" y="104">MAR</text><text x="70" y="104">APR</text><text x="90" y="104">MAY</text><text x="110" y="104">JUN</text><text x="130" y="104">JUL</text><text x="148" y="104">AUG</text></g>
    <g stroke="#eee" stroke-width=".4"><line x1="6" y1="22" x2="166" y2="22"/><line x1="6" y1="44" x2="166" y2="44"/><line x1="6" y1="66" x2="166" y2="66"/><line x1="6" y1="88" x2="166" y2="88"/></g>
    <line x1="6" y1="99" x2="166" y2="99" stroke="#bbb" stroke-width=".4"/>
    <path d="M12 90 C25 60 30 85 48 72 S80 62 95 55 S120 90 135 70 S150 40 160 30" fill="none" stroke="#c5c7cc" stroke-width=".8"/>
    <path d="M12 90 L32 82 L50 78 L72 72 L95 68 L112 60 L135 80 L160 28" fill="none" stroke="#e5232b" stroke-width=".8"/>
    <g fill="#fff" stroke="#e5232b" stroke-width=".5"><circle cx="12" cy="90" r="1.3"/><circle cx="32" cy="82" r="1.3"/><circle cx="50" cy="78" r="1.3"/><circle cx="72" cy="72" r="1.3"/><circle cx="95" cy="68" r="1.3"/><circle cx="112" cy="60" r="1.3"/><circle cx="135" cy="80" r="1.3"/><circle cx="160" cy="28" r="1.3"/></g>
    <rect x="102" y="46" width="14" height="5" fill="#262a35"/><text x="104" y="49.5" font-size="2.5" fill="#fff">43%</text>
  </svg>
  <div style="left:193px;top:40px;width:89px;height:94px;background:var(--red);color:#fff">
    <p style="position:absolute;left:5px;top:5px;font-size:3.5px;margin:0">Tue 8 Aug</p>
    <p style="position:absolute;left:5px;top:18px;font:700 10px 'Open Sans',sans-serif;margin:0">75.8<small style="font-size:5px">M</small></p>
    <p style="position:absolute;left:53px;top:18px;font-size:3px;line-height:1.3;margin:0">+34.55<br>07.65%</p>
    <div style="position:absolute;right:5px;top:16px;width:11px;height:12px;border:.6px solid #fff;font-size:8px;text-align:center;line-height:11px">↑</div>
    <div style="position:absolute;left:5px;right:5px;top:34px;height:.4px;background:#f48a8e"></div>
    <table style="position:absolute;left:5px;top:45px;width:79px;font-size:3.2px;border-collapse:collapse;color:#fff">
      <tr><td style="padding-bottom:4px">Toronto</td><td style="text-align:right">+ 43.05%</td></tr>
      <tr><td style="padding-bottom:4px">Montreal</td><td style="text-align:right">+ 25.73%</td></tr>
      <tr><td style="padding-bottom:4px">Vancouver</td><td style="text-align:right">+ 8.15%</td></tr>
      <tr><td>Ottawa</td><td style="text-align:right">+ 5.48%</td></tr>
    </table>
  </div>
  <footer class="foot">www.brightlaneskills.com<span class="page">13</span></footer>
</section>

<!-- 14 bar chart -->
<section class="slide c2 r4">
  <div class="mark"><i></i><i></i><i></i></div>
  <h2 class="title"><b>Data</b> Driven</h2>
  <div class="tag">BRIGHTLANE<br>SKILLS</div>
  <svg style="left:18px;top:40px" width="262" height="90" viewBox="0 0 262 90" aria-label="Bar chart with three series over four years">
    <g font-size="2.6" fill="#8b8e95" font-family="Open Sans"><rect x="190" y="1" width="2" height="2" fill="#262a35"/><text x="193" y="3">Series 1</text><rect x="206" y="1" width="2" height="2" fill="#e5232b"/><text x="209" y="3">Series 2</text><rect x="222" y="1" width="2" height="2" fill="#9a9ca3"/><text x="225" y="3">Series 3</text>
      <text x="0" y="16">5</text><text x="0" y="29">4</text><text x="0" y="42">3</text><text x="0" y="55">2</text><text x="0" y="68">1</text><text x="0" y="81">0</text></g>
    <line x1="6" y1="80" x2="260" y2="80" stroke="#ccc" stroke-width=".4"/>
    <g fill="#262a35"><rect x="20" y="35" width="9" height="45"/><rect x="85" y="42" width="9" height="38"/><rect x="145" y="48" width="9" height="32"/><rect x="200" y="33" width="9" height="47"/></g>
    <g fill="#e5232b"><rect x="31" y="57" width="9" height="23"/><rect x="96" y="30" width="9" height="50"/><rect x="156" y="62" width="9" height="18"/><rect x="211" y="50" width="9" height="30"/></g>
    <g fill="#c4c6cb"><rect x="42" y="62" width="9" height="18"/><rect x="107" y="60" width="9" height="20"/><rect x="167" y="44" width="9" height="36"/><rect x="222" y="23" width="9" height="57"/></g>
    <g font-size="2.4" fill="#aaa"><text x="30" y="85">2015</text><text x="95" y="85">2016</text><text x="155" y="85">2017</text><text x="210" y="85">2018</text></g>
  </svg>
  <p class="num" style="left:30px;top:122px;font:400 11px 'Roboto Slab',serif;color:var(--navy)">01</p>
  <div class="pack" style="left:58px;top:123px;text-align:left;width:50px">ORGANIZE PACK<span class="tiny">Short note for this item</span></div>
  <p class="num" style="left:131px;top:122px;font:400 11px 'Roboto Slab',serif;color:var(--navy)">02</p>
  <div class="pack" style="left:160px;top:123px;text-align:left;width:50px">ORGANIZE PACK<span class="tiny">Short note for this item</span></div>
  <p class="num" style="left:212px;top:122px;font:400 11px 'Roboto Slab',serif;color:var(--navy)">03</p>
  <div class="pack" style="left:240px;top:123px;text-align:left;width:46px">ORGANIZE PACK<span class="tiny">Short note for this item</span></div>
  <footer class="foot">www.brightlaneskills.com<span class="page">14</span></footer>
</section>

<!-- 15 donuts -->
<section class="slide c3 r4">
  <div class="mark"><i></i><i></i><i></i></div>
  <h2 class="title"><b>Data</b> Driven</h2>
  <div class="tag">BRIGHTLANE<br>SKILLS</div>
  <svg style="left:0;top:0" width="294" height="166" viewBox="0 0 294 166" aria-label="Three ring charts showing 35, 50 and 65 percent">
    <g fill="none" stroke-width="2.5">
      <circle cx="58" cy="62" r="19" stroke="#e6e7ea"/><circle cx="58" cy="62" r="19" stroke="#9a9ca3" stroke-dasharray="41.8 119.4" transform="rotate(-90 58 62)"/>
      <circle cx="147" cy="62" r="19" stroke="#e6e7ea"/><circle cx="147" cy="62" r="19" stroke="#e5232b" stroke-dasharray="59.7 119.4" transform="rotate(-90 147 62)"/>
      <circle cx="236" cy="62" r="19" stroke="#e6e7ea"/><circle cx="236" cy="62" r="19" stroke="#ef6a2b" stroke-dasharray="77.6 119.4" transform="rotate(-90 236 62)"/>
    </g>
    <g fill="#e5232b"><circle cx="70" cy="47" r="4.5"/><circle cx="159" cy="47" r="4.5"/><circle cx="248" cy="47" r="4.5"/></g>
    <g font-family="Open Sans" text-anchor="middle"><text x="58" y="65" font-size="9" fill="#555">35<tspan font-size="5">%</tspan></text><text x="147" y="65" font-size="9" fill="#555">50<tspan font-size="5">%</tspan></text><text x="236" y="65" font-size="9" fill="#555">65<tspan font-size="5">%</tspan></text>
      <text x="58" y="70" font-size="2" fill="#e5232b">FACT NUMBER</text><text x="147" y="70" font-size="2" fill="#e5232b">FACT NUMBER</text><text x="236" y="70" font-size="2" fill="#e5232b">FACT NUMBER</text></g>
  </svg>
  <div class="pack" style="left:28px;top:95px;width:60px;font-size:4px">$ 1,635,000<span class="tiny">Short note to sum up this figure</span></div>
  <div class="pack" style="left:117px;top:95px;width:60px;font-size:4px">$ 1,250,000<span class="tiny">Short note to sum up this figure</span></div>
  <div class="pack" style="left:206px;top:95px;width:60px;font-size:4px">$ 2,125,000<span class="tiny">Short note to sum up this figure</span></div>
  <footer class="foot">www.brightlaneskills.com<span class="page">15</span></footer>
</section>

<!-- 16 fact number -->
<section class="slide c4 r4">
  <div class="mark"><i></i><i></i><i></i></div>
  <h2 class="title"><b>The Fact</b> Number</h2>
  <div class="tag">BRIGHTLANE<br>SKILLS</div>
  <svg style="left:0;top:0" width="294" height="166" viewBox="0 0 294 166" aria-hidden="true">
    <g fill="#262a35" stroke="#cfd1d6" stroke-width="1.2"><circle cx="64" cy="74" r="26"/><circle cx="146" cy="74" r="31"/><circle cx="227" cy="74" r="26"/></g>
    <g fill="none" stroke="#262a35" stroke-width=".5"><circle cx="64" cy="74" r="28"/><circle cx="146" cy="74" r="33"/><circle cx="227" cy="74" r="28"/></g>
    <g font-family="Open Sans" text-anchor="middle"><text x="64" y="73" font-size="11" fill="#fff">45<tspan font-size="6">K</tspan></text><text x="146" y="71" font-size="12" fill="#fff">+30<tspan font-size="6">%</tspan></text><text x="227" y="73" font-size="11" fill="#fff">76<tspan font-size="6">H</tspan></text>
      <text x="64" y="79" font-size="2.5" fill="#e5232b">ORGANIZE PACK</text><text x="146" y="78" font-size="2.5" fill="#e5232b">ORGANIZE PACK</text><text x="227" y="79" font-size="2.5" fill="#e5232b">ORGANIZE PACK</text>
      <g font-size="2.1" fill="#a7aab2"><text x="64" y="84">Short note on it</text><text x="146" y="84">Short note on it</text><text x="227" y="84">Short note on it</text></g></g>
  </svg>
  <p class="tiny" style="left:55px;right:30px;top:128px;text-align:center">Numbers help a group see the size of a risk. Use one clear figure per circle and keep the detail in the notes so the trainer can explain it out loud.</p>
  <footer class="foot">www.brightlaneskills.com<span class="page">16</span></footer>
</section>

<!-- 17 timeline -->
<section class="slide c1 r5">
  <div class="mark"><i></i><i></i><i></i></div>
  <h2 class="title"><b>Timeline</b> Concept</h2>
  <div class="tag">BRIGHTLANE<br>SKILLS</div>
  <svg style="left:0;top:0" width="294" height="166" viewBox="0 0 294 166" aria-label="Timeline at 25, 35, 40 and 55 percent">
    <g font-family="Open Sans" font-size="9" fill="#3a3d45" text-anchor="middle"><text x="41" y="52">25<tspan font-size="6">%</tspan></text><text x="106" y="52">35<tspan font-size="6">%</tspan></text><text x="172" y="52">40<tspan font-size="6">%</tspan></text><text x="238" y="52">55<tspan font-size="6">%</tspan></text></g>
    <rect x="20" y="63" width="50" height="3" fill="#262a35"/><rect x="70" y="63" width="70" height="3" fill="#9a9ca3"/><rect x="140" y="63" width="75" height="3" fill="#e5232b"/><rect x="215" y="63" width="63" height="3" fill="#e5232b"/>
    <polygon points="38,62 44,62 41,57" fill="#262a35"/><polygon points="103,62 109,62 106,57" fill="#9a9ca3"/><polygon points="169,62 175,62 172,57" fill="#e5232b"/><polygon points="235,62 241,62 238,57" fill="#e5232b"/>
    <g stroke="#eee" stroke-width=".4"><line x1="85" y1="75" x2="85" y2="140"/><line x1="150" y1="75" x2="150" y2="140"/><line x1="215" y1="75" x2="215" y2="140"/></g>
    <g fill="#e5232b"><path d="M37 99 l4 -4 4 4 v4 h-8z"/><rect x="102" y="96" width="8" height="6" rx=".8"/><circle cx="172" cy="99" r="3.5"/><path d="M238 99 v-4 a4 4 0 1 0 4 4z"/></g>
  </svg>
  <div class="pack" style="left:14px;top:114px;width:55px">ORGANIZE PACK<span class="tiny">Short note for this stage</span></div>
  <div class="pack" style="left:79px;top:114px;width:55px">ORGANIZE PACK<span class="tiny">Short note for this stage</span></div>
  <div class="pack" style="left:145px;top:114px;width:55px">ORGANIZE PACK<span class="tiny">Short note for this stage</span></div>
  <div class="pack" style="left:210px;top:114px;width:55px">ORGANIZE PACK<span class="tiny">Short note for this stage</span></div>
  <footer class="foot">www.brightlaneskills.com<span class="page">17</span></footer>
</section>

<!-- 18 table -->
<section class="slide c2 r5">
  <div class="mark"><i></i><i></i><i></i></div>
  <h2 class="title"><b>Simple</b> Table</h2>
  <div class="tag">BRIGHTLANE<br>SKILLS</div>
  <table class="grid-table" style="left:20px;top:38px">
    <tr><td class="feat" rowspan="2" style="font-size:4px">PRODUCT FEATURES</td><th>BASIC</th><th>STANDARD</th><th>PROFESSIONAL</th><th>ULTIMATE</th></tr>
    <tr><th style="font-size:4px;background:#b7b9bd">$500</th><th style="font-size:4px;background:#b7b9bd">$1000</th><th style="font-size:4px;background:#b7b9bd">$1500</th><th style="font-size:4px;background:#b7b9bd">$2000</th></tr>
    <tr><td class="feat">SITE INDUCTION</td><td>Lorem</td><td>Ipsum</td><td>Dolor</td><td>Amet</td></tr>
    <tr><td class="feat">TOOLBOX TALKS</td><td class="no">✕</td><td class="ok">✓</td><td class="ok">✓</td><td class="ok">✓</td></tr>
    <tr><td class="feat">FIRST AID REFRESH</td><td class="no">✕</td><td class="ok">✓</td><td class="ok">✓</td><td class="ok">✓</td></tr>
    <tr><td class="feat">MANUAL HANDLING</td><td class="no">✕</td><td class="no">✕</td><td class="ok">✓</td><td class="ok">✓</td></tr>
    <tr><td class="feat">WORK AT HEIGHT</td><td>1 Project</td><td>3 Project</td><td>5 Project</td><td>10 Project</td></tr>
    <tr><td class="feat">CONFINED SPACE</td><td>1 Month</td><td>6 Month</td><td>1 Year</td><td>Unlimited</td></tr>
    <tr><td class="feat">PLANT OPERATION</td><td>1 Year</td><td>2 Year</td><td>5 Year</td><td>Unlimited</td></tr>
  </table>
  <p class="tiny" style="left:20px;top:141px;width:255px">Compare each course pack at a glance. Keep the full detail, pricing notes and terms in the speaker notes so the trainer can talk the group through it.</p>
  <footer class="foot">www.brightlaneskills.com<span class="page">18</span></footer>
</section>

<!-- 19 partners -->
<section class="slide c3 r5">
  <div class="mark"><i></i><i></i><i></i></div>
  <h2 class="title"><b>Valuable</b> Partners</h2>
  <div class="tag">BRIGHTLANE<br>SKILLS</div>
  <svg style="left:20px;top:42px" width="256" height="90" viewBox="0 0 256 90" aria-label="Grid of partner badges">
    <g stroke="#e6e7ea" stroke-width=".5" fill="none"><line x1="64" y1="0" x2="64" y2="90"/><line x1="128" y1="0" x2="128" y2="90"/><line x1="192" y1="0" x2="192" y2="90"/><line x1="0" y1="30" x2="256" y2="30"/><line x1="0" y1="60" x2="256" y2="60"/><rect x="0" y="0" width="256" height="90"/></g>
    <g fill="#d4d6da">
      <rect x="20" y="11" width="24" height="8" rx="1.5"/><rect x="84" y="11" width="24" height="8" rx="1.5"/><rect x="148" y="11" width="24" height="8" rx="1.5"/><rect x="212" y="11" width="24" height="8" rx="1.5"/>
      <rect x="20" y="41" width="24" height="8" rx="1.5"/><rect x="84" y="41" width="24" height="8" rx="1.5"/><rect x="148" y="41" width="24" height="8" rx="1.5"/><rect x="212" y="41" width="24" height="8" rx="1.5"/>
      <rect x="20" y="71" width="24" height="8" rx="1.5"/><rect x="84" y="71" width="24" height="8" rx="1.5"/><rect x="148" y="71" width="24" height="8" rx="1.5"/><rect x="212" y="71" width="24" height="8" rx="1.5"/>
    </g>
  </svg>
  <p class="tiny" style="left:20px;top:136px;width:256px">We work with leading groups across mining, manufacturing and building. Add a partner badge to each cell and keep the list short so the room can read it.</p>
  <footer class="foot">www.brightlaneskills.com<span class="page">19</span></footer>
</section>

<!-- 20 thank you -->
<section class="slide c4 r5">
  <div class="bars" style="left:20px;top:0;height:112px"><i></i><i></i></div>
  <div class="tag">BRIGHTLANE<br>SKILLS</div>
  <div class="brand brand-stack" style="left:20px;top:119px"><i></i><span>BRIGHTLANE<br>SKILLS</span></div>
  <p class="byline" style="left:20px;top:138px">PlanWell. MoveWell. BuildWell.</p>
  <div style="left:89px;top:118px;width:.5px;height:24px;background:var(--line)"></div>
  <h2 style="left:95px;top:120px;font:400 8px 'Roboto Slab',serif;color:var(--navy)">Thank You</h2>
  <p class="tiny" style="left:95px;top:131px;width:100px">Questions are welcome. Thank you for taking part and for keeping each other safe on site.</p>
  <footer class="foot">www.brightlaneskills.com<span class="page">20</span></footer>
</section>

</body>
</html>
```